Accounting company website and Social page design

I need a website designed and copy written for an accounting/bookkeeping company in Ohio. We have content but would need someone to fine-tune it and make it sound good. I also need a Social page design created. Attached is the logo for the company.

```html
<!DOCTYPE html>
<html lang="en">
<head>
<meta charset="utf-8">
<title>Keystone Group — Accounting, Bookkeeping and Tax Prep</title>
<link rel="stylesheet" href="https://fonts.googleapis.com/css2?family=Cinzel:wght@400;600;700&family=Poppins:wght@400;500;600;800&display=swap">
<style>
:root{
  --gold:#e9a21a;
  --gold-deep:#d88f0d;
  --ink:#3b3d47;
  --ink-soft:#2d2f37;
  --cream:#fdf5e6;
  --text:#5a5a5a;
  --white:#ffffff;
}
*{box-sizing:border-box;margin:0;padding:0}
html,body{width:1200px;height:3458px;overflow:hidden}
body{position:relative;background:var(--white);font-family:"Poppins",sans-serif;color:var(--text)}
.abs{position:absolute}
.serif{font-family:"Cinzel",serif}
.btn{position:absolute;display:flex;align-items:center;justify-content:center;background:var(--gold);color:var(--white);font-family:"Cinzel",serif;font-weight:700;font-size:17px;letter-spacing:1px;border-radius:8px}
.photo{position:absolute}

/* header */
.site-header{position:absolute;left:0;top:0;width:1200px;height:100px}
.brand{position:absolute;left:60px;top:26px;display:flex;align-items:center;gap:8px}
.brand-dot{width:14px;height:14px;border-radius:50%;background:var(--gold)}
.brand-name{font-family:"Cinzel",serif;font-weight:600;font-size:24px;color:var(--ink);letter-spacing:.5px}
.main-nav{position:absolute;left:634px;top:24px;display:flex;gap:22px;font-size:11.5px;color:var(--ink)}
.main-nav .active{color:var(--gold)}
.call{position:absolute;left:986px;top:12px;display:flex;align-items:center;gap:10px}
.call-ring{width:38px;height:38px;border:2px solid var(--gold);border-radius:50%;display:flex;align-items:center;justify-content:center}
.call small{display:block;color:var(--gold);font-size:10.5px}
.call b{font-family:"Cinzel",serif;font-weight:400;color:var(--ink);font-size:17px}

/* hero */
.hero-photo{left:0;top:60px;width:1200px;height:645px;background:linear-gradient(180deg,#b99a93 0%,#c9a896 22%,#8a7462 42%,#4c4a33 65%,#33381f 100%)}
.hero-title{position:absolute;left:62px;top:200px;font-weight:800;font-size:49px;line-height:50px;color:var(--ink)}
.hero-title span{color:var(--gold)}
.slider-arrow{position:absolute;width:40px;height:40px;border-radius:50%;display:flex;align-items:center;justify-content:center}

/* welcome */
.eyebrow{left:148px;top:788px;color:var(--gold);font-size:14px;font-weight:600;letter-spacing:1px}
.section-title{font-family:"Cinzel",serif;color:var(--ink);font-weight:400}
.welcome p{position:absolute;left:153px;width:433px;font-size:11.6px;line-height:19.6px;color:var(--text)}

/* services */
.card{position:absolute;top:1474px;width:322px;height:452px;background:var(--white);border-radius:10px;overflow:hidden;box-shadow:0 4px 14px rgba(0,0,0,.05)}
.card .photo{left:0;top:0;width:322px;height:208px}
.card-icon{position:absolute;left:129px;top:155px;width:64px;height:64px;border-radius:50%;background:var(--white);border:2px solid var(--gold);display:flex;align-items:center;justify-content:center}
.card h3{position:absolute;top:238px;width:100%;text-align:center;font-family:"Cinzel",serif;font-size:20px;font-weight:600;color:var(--ink);letter-spacing:1px}
.card p{position:absolute;top:284px;left:28px;width:266px;text-align:center;font-size:11.4px;line-height:19.5px}
.card .btn{left:80px;top:381px;width:161px;height:41px}

/* cta */
.cta-title{position:absolute;left:0;top:2147px;width:1200px;text-align:center;font-family:"Cinzel",serif;font-weight:700;font-size:34px;line-height:42px;color:var(--white);letter-spacing:1px}
.cta-sub{position:absolute;left:0;top:2232px;width:1200px;text-align:center;color:#fff3d6;font-size:12.5px}

/* news */
.news-item .photo{left:60px;width:135px;height:105px;border-radius:8px}
.news-date{position:absolute;left:226px;color:var(--gold);font-size:11px}
.news-head{position:absolute;left:226px;font-family:"Cinzel",serif;font-weight:700;font-size:15px;color:var(--ink);letter-spacing:.5px}
.news-text{position:absolute;left:227px;width:320px;font-size:11.5px;line-height:19.5px}

/* social widget */
.feed{position:absolute;left:650px;top:2523px;width:360px;height:353px;border:1.5px solid var(--gold);background:var(--white)}

/* pre-footer band */
.footer-band{position:absolute;left:0;top:2930px;width:1200px;height:209px;background:linear-gradient(180deg,#ffffff 0%,#fdf1d8 55%,#f6d68f 100%)}

/* footer */
.site-footer{position:absolute;left:0;top:3147px;width:1200px;height:311px;background:var(--ink)}
.foot-head{position:absolute;top:58px;font-family:"Cinzel",serif;color:var(--white);font-size:16px;letter-spacing:1px}
.foot-list{position:absolute;top:94px;list-style:none;font-size:12px;color:#e8e8ea}
.foot-list li{height:22.6px;display:flex;align-items:center}
.foot-list li::before{content:"";width:5px;height:5px;border-radius:50%;background:var(--gold);margin-right:12px}
.foot-contact{position:absolute;left:899px;display:flex;gap:14px;color:#e8e8ea;font-size:12px;line-height:18px}
</style>
</head>
<body>

<!-- header -->
<header class="site-header">
  <svg class="abs" style="left:0;top:0" width="1200" height="100" viewBox="0 0 1200 100">
    <polygon points="0,0 1200,0 1200,60 255,60 218,97 0,97" fill="#fff"/>
    <polyline points="1200,60 255,60 218,97 0,97" fill="none" stroke="#e9a21a" stroke-width="2.5"/>
  </svg>
  <div class="brand"><span class="brand-dot"></span><span class="brand-name">Keystone Group</span></div>
  <nav class="main-nav">
    <span class="active">HOME</span><span>ABOUT</span><span>SERVICES</span><span>NEWS</span><span>CONTACT US</span>
  </nav>
  <svg class="abs" style="left:645px;top:42px" width="10" height="6"><polygon points="0,0 10,0 5,6" fill="#e9a21a"/></svg>
  <div class="call">
    <div class="call-ring">
      <svg width="18" height="18" viewBox="0 0 24 24"><path d="M6.6 10.8a15 15 0 0 0 6.6 6.6l2.2-2.2c.3-.3.7-.4 1-.2 1.1.4 2.3.6 3.6.6.6 0 1 .4 1 1V20c0 .6-.4 1-1 1A17 17 0 0 1 3 4c0-.6.4-1 1-1h3.5c.6 0 1 .4 1 1 0 1.3.2 2.5.6 3.6.1.3 0 .7-.2 1z" fill="none" stroke="#e9a21a" stroke-width="1.6"/></svg>
    </div>
    <div><small>CALL US :</small><b>123 456 7890</b></div>
  </div>
</header>

<!-- hero -->
<section class="hero">
  <div class="photo hero-photo" role="img" aria-label="Woman working on a laptop on a wooden balcony overlooking hills at sunset"></div>
  <h1 class="hero-title">You Run Your<br>Business<br><span>We’ll Handle Your<br>Finances</span></h1>
  <div class="btn" style="left:60px;top:423px;width:164px;height:43px;font-size:16px">CONTACT US</div>
  <div class="slider-arrow" style="left:1121px;top:318px;background:#3b3d47">
    <svg width="12" height="14"><polyline points="8,1 2,7 8,13" fill="none" stroke="#fff" stroke-width="2"/></svg></div>
  <div class="slider-arrow" style="left:1121px;top:366px;background:rgba(59,61,71,.35)">
    <svg width="12" height="14"><polyline points="4,1 10,7 4,13" fill="none" stroke="#fff" stroke-width="2"/></svg></div>
  <div class="abs" style="left:0;top:705px;width:1200px;height:6px;background:var(--gold)"></div>
</section>

<!-- welcome -->
<section class="welcome">
  <div class="abs eyebrow serif">WELCOME TO</div>
  <h2 class="abs section-title" style="left:147px;top:812px;font-size:39px">KEYSTONE GROUP</h2>
  <div class="abs" style="left:555px;top:837px;width:32px;height:2px;background:var(--gold)"></div>
  <p style="top:878px">Lorem Ipsum has been the industry’s standard dummy text ever since the 1500s, when an unknown printer took a galley of type and scrambled it to make a type specimen book. It has survived not only five centuries, but also the leap into electronic typesetting, remaining essentially</p>
  <p style="top:972px">Lorem Ipsum has been the industry’s standard dummy text ever since the 1500s, when an unknown printer took a galley of type and scrambled it to make a type specimen book. It has survived not only five centuries, but also the leap into electronic typesetting, remaining essentially unchanged. It was popularised in the 1960s with the release of Letraset sheets containing Lorem Ipsum passages, and more recently with desktop.</p>
  <div class="btn" style="left:153px;top:1109px;width:161px;height:41px">LEARN MORE</div>
  <div class="abs" style="left:736px;top:787px;width:326px;height:326px;border-radius:50%;border:2px solid var(--gold)"></div>
  <div class="photo" role="img" aria-label="Woman in glasses working at a laptop in a bright office" style="left:744px;top:795px;width:310px;height:310px;border-radius:50%;background:radial-gradient(circle at 60% 40%,#f4efe9,#d9cfc4 60%,#a89a8b)"></div>
  <div class="photo" role="img" aria-label="Hand with pencil over printed financial figures and a calculator" style="left:673px;top:1003px;width:178px;height:178px;border-radius:50%;border:6px solid var(--gold);background:radial-gradient(circle at 45% 45%,#eef0f3,#b9c0ca 60%,#69707c)"></div>
</section>

<!-- services -->
<section class="services">
  <svg class="abs" style="left:0;top:1266px" width="1200" height="725" viewBox="0 0 1200 725">
    <polygon points="0,100 1200,140 1200,720 0,720" fill="#fdf5e6"/>
  </svg>
  <div class="abs" style="left:416px;top:1423px;width:32px;height:2px;background:var(--gold)"></div>
  <h2 class="abs section-title" style="left:0;top:1398px;width:1200px;text-align:center;font-size:39px">OUR SERVICES</h2>
  <div class="abs" style="left:749px;top:1423px;width:32px;height:2px;background:var(--gold)"></div>

  <article class="card" style="left:86px">
    <div class="photo" role="img" aria-label="Hands using a calculator over financial reports" style="background:linear-gradient(135deg,#cfd3d8,#8d939c 55%,#4d5058)"></div>
    <svg class="abs" style="left:0;top:150px" width="322" height="60"><polygon points="0,60 322,35 322,60" fill="#fff"/><polygon points="0,60 322,30 322,36 0,60" fill="#e9a21a"/></svg>
    <div class="card-icon"><svg width="30" height="30" viewBox="0 0 30 30" fill="none" stroke="#3b3d47" stroke-width="1.5"><rect x="6" y="3" width="18" height="24" rx="2"/><rect x="9" y="6" width="12" height="5"/><rect x="9" y="14" width="3" height="3"/><rect x="14" y="14" width="3" height="3"/><rect x="9" y="20" width="3" height="3"/><circle cx="21" cy="22" r="4" stroke="#e9a21a"/></svg></div>
    <h3>ACCOUNTING</h3>
    <p>Lorem Ipsum has been the industry’s standard dummy text ever since thes, when an unknown printer took a galley of type and scrambled it to make a type specimen book.</p>
    <div class="btn">LEARN MORE</div>
  </article>

  <article class="card" style="left:439px">
    <div class="photo" role="img" aria-label="Person reviewing charts on a laptop beside a coffee cup" style="background:linear-gradient(135deg,#f1f1ef,#c9cbc7 55%,#8c8f89)"></div>
    <svg class="abs" style="left:0;top:150px" width="322" height="60"><polygon points="0,60 322,35 322,60" fill="#fff"/><polygon points="0,60 322,30 322,36 0,60" fill="#e9a21a"/></svg>
    <div class="card-icon"><svg width="30" height="30" viewBox="0 0 30 30" fill="none" stroke="#3b3d47" stroke-width="1.5"><rect x="3" y="5" width="24" height="16" rx="1"/><line x1="11" y1="26" x2="19" y2="26"/><line x1="15" y1="21" x2="15" y2="26"/><circle cx="10" cy="12" r="3" stroke="#e9a21a"/><line x1="16" y1="10" x2="23" y2="10"/><line x1="16" y1="14" x2="23" y2="14"/></svg></div>
    <h3>BOOKKEEPING</h3>
    <p>Lorem Ipsum has been the industry’s standard dummy text ever since thes, when an unknown printer took a galley of type and scrambled it to make a type specimen book.</p>
    <div class="btn">LEARN MORE</div>
  </article>

  <article class="card" style="left:792px">
    <div class="photo" role="img" aria-label="Two women working together at a desk near a wooden staircase" style="background:linear-gradient(135deg,#c99a6c,#a5795a 50%,#5d5245)"></div>
    <svg class="abs" style="left:0;top:150px" width="322" height="60"><polygon points="0,60 322,35 322,60" fill="#fff"/><polygon points="0,60 322,30 322,36 0,60" fill="#e9a21a"/></svg>
    <div class="card-icon"><svg width="30" height="30" viewBox="0 0 30 30" fill="none" stroke="#3b3d47" stroke-width="1.5"><rect x="5" y="3" width="16" height="22" rx="1"/><line x1="8" y1="12" x2="18" y2="12"/><line x1="8" y1="16" x2="18" y2="16"/><line x1="8" y1="20" x2="14" y2="20"/><rect x="17" y="16" width="9" height="11" stroke="#e9a21a"/><text x="7" y="9" font-size="5" fill="#3b3d47" stroke="none" font-family="Poppins,sans-serif">TAX</text></svg></div>
    <h3>TAX PREP</h3>
    <p>Lorem Ipsum has been the industry’s standard dummy text ever since thes, when an unknown printer took a galley of type and scrambled it to make a type specimen book.</p>
    <div class="btn">LEARN MORE</div>
  </article>
</section>

<!-- call to action -->
<section class="cta">
  <svg class="abs" style="left:0;top:1975px" width="1200" height="415" viewBox="0 0 1200 415">
    <defs><linearGradient id="ctaFill" x1="0" y1="0" x2="0" y2="1"><stop offset="0" stop-color="#e3a21d"/><stop offset="1" stop-color="#d8930e"/></linearGradient></defs>
    <polygon points="0,8 1200,70 1200,415 0,415" fill="url(#ctaFill)"/>
    <line x1="0" y1="0" x2="1200" y2="62" stroke="#e9a21a" stroke-width="2"/>
  </svg>
  <h2 class="cta-title">UPDATE YOUR TEXT EXPERIENCE<br>WITH KEYSTONE GROUP</h2>
  <p class="cta-sub">Lorem Ipsum has been the industry’s standard dummy text ever since the.</p>
  <div class="btn" style="left:432px;top:2271px;width:164px;height:44px;border:1.5px solid #fff;font-weight:600;font-size:18px;gap:8px">
    <svg width="20" height="20" viewBox="0 0 24 24"><path d="M6.6 10.8a15 15 0 0 0 6.6 6.6l2.2-2.2c.3-.3.7-.4 1-.2 1.1.4 2.3.6 3.6.6.6 0 1 .4 1 1V20c0 .6-.4 1-1 1A17 17 0 0 1 3 4c0-.6.4-1 1-1h3.5c.6 0 1 .4 1 1 0 1.3.2 2.5.6 3.6.1.3 0 .7-.2 1z" fill="none" stroke="#fff" stroke-width="1.6"/></svg>123 456 7890</div>
  <div class="btn" style="left:607px;top:2271px;width:160px;height:44px;background:var(--ink)">CONTACT US</div>
</section>

<!-- news -->
<section class="news">
  <h2 class="abs section-title" style="left:62px;top:2455px;font-size:39px">NEWS</h2>
  <div class="abs" style="left:185px;top:2480px;width:32px;height:2px;background:var(--gold)"></div>
  <div class="abs" style="left:587px;top:2470px;width:3px;height:440px;background:linear-gradient(90deg,rgba(0,0,0,.06),rgba(0,0,0,0))"></div>

  <div class="news-item">
    <div class="photo" role="img" aria-label="Two colleagues working at a desk" style="top:2530px;background:linear-gradient(135deg,#c79a6e,#8f7661)"></div>
    <div class="news-date" style="top:2536px">20 OCT 2022</div>
    <div class="news-head" style="top:2556px">LOREM IPSUM SIMPLE TEXT PRINT</div>
    <div class="news-text" style="top:2586px">Lorem Ipsum has been the industry’s standard dummy text ever since thes, when an unknown printer.</div>
  </div>
  <div class="news-item">
    <div class="photo" role="img" aria-label="Hourglass on a pale background" style="top:2657px;background:linear-gradient(135deg,#e7ebf0,#a9b3c0)"></div>
    <div class="news-date" style="top:2664px">20 OCT 2022</div>
    <div class="news-head" style="top:2684px">LOREM IPSUM SIMPLE TEXT PRINT</div>
    <div class="news-text" style="top:2714px">Lorem Ipsum has been the industry’s standard dummy text ever since thes, when an unknown printer.</div>
  </div>
  <div class="news-item">
    <div class="photo" role="img" aria-label="Hands reviewing printed charts with a pen" style="top:2785px;background:linear-gradient(135deg,#b8c4d4,#4f5d72)"></div>
    <div class="news-date" style="top:2791px">20 OCT 2022</div>
    <div class="news-head" style="top:2811px">LOREM IPSUM SIMPLE TEXT PRINT</div>
    <div class="news-text" style="top:2841px">Lorem Ipsum has been the industry’s standard dummy text ever since thes, when an unknown printer.</div>
  </div>
</section>

<!-- social feed -->
<section class="social">
  <h2 class="abs section-title" style="left:648px;top:2455px;font-size:39px">SOCIAL</h2>
  <div class="abs" style="left:812px;top:2480px;width:32px;height:2px;background:var(--gold)"></div>
  <div class="feed">
    <div class="abs" style="left:20px;top:16px;width:60px;height:60px;border:1px solid #ddd;border-radius:4px;display:flex;align-items:center;justify-content:center"><span style="width:16px;height:16px;border-radius:50%;background:var(--gold)"></span></div>
    <div class="abs serif" style="left:95px;top:16px;color:var(--gold);font-size:15px">KEYSTONE GROUP</div>
    <div class="abs" style="left:96px;top:40px;font-size:11px">134 likes</div>
    <div class="photo" role="img" aria-label="Hand holding a phone over colourful bar charts" style="left:20px;top:90px;width:318px;height:70px;background:linear-gradient(90deg,#c8d6c8,#e9ece6 45%,#6a8fb5)"></div>
    <div class="abs" style="left:21px;top:166px;font-size:10px;color:var(--gold)">Embed</div>
    <div class="abs" style="left:234px;top:166px;font-size:10px;color:var(--gold)">View on page</div>
    <div class="abs" style="left:20px;top:188px;width:318px;height:1px;background:#eee"></div>
    <div class="abs" style="left:24px;top:208px;width:40px;height:40px;border-radius:50%;background:var(--gold)"></div>
    <div class="abs" style="left:81px;top:210px;width:200px;font-size:12.5px;line-height:18px;color:var(--ink);font-weight:500">Lorem Ipsum Has Been The Standard Dummy Text</div>
    <div class="abs" style="left:292px;top:211px;font-size:11px;color:var(--gold)">5h ago</div>
    <div class="abs" style="left:82px;top:257px;font-size:11px">2 days ago at 8:30am</div>
    <div class="abs" style="left:80px;top:288px;width:54px;height:20px;border:1px solid var(--gold);border-radius:2px;font-size:10px;color:var(--gold);display:flex;align-items:center;justify-content:center">Like</div>
    <div class="abs" style="left:138px;top:288px;width:61px;height:20px;border:1px solid var(--gold);border-radius:2px;font-size:10px;color:var(--gold);display:flex;align-items:center;justify-content:center">Love</div>
  </div>
</section>

<!-- pre-footer decorative band -->
<div class="footer-band" role="img" aria-label="Golden sunburst decoration rising above the footer"></div>

<!-- footer -->
<footer class="site-footer">
  <div class="abs" style="left:0;top:-8px;width:1200px;height:8px;background:var(--gold)"></div>
  <div class="abs" style="left:60px;top:70px;display:flex;align-items:center;gap:8px">
    <span style="width:14px;height:14px;border-radius:50%;background:var(--gold)"></span>
    <span class="serif" style="color:#fff;font-size:24px;font-weight:600">Keystone Group</span>
  </div>
  <div class="abs" style="left:60px;top:169px;width:255px;height:35px;background:#fff;border-radius:6px;font-size:11px;color:#777;display:flex;align-items:center;padding-left:14px">Enter Email *</div>
  <div class="abs" style="left:277px;top:169px;width:38px;height:35px;background:var(--gold);border-radius:0 6px 6px 0;display:flex;align-items:center;justify-content:center">
    <svg width="18" height="18" viewBox="0 0 24 24"><path d="M2 11 22 3 15 21l-3-7z" fill="#3b3d47"/></svg></div>

  <div class="abs" style="left:611px;top:40px;width:1px;height:240px;background:rgba(255,255,255,.07)"></div>
  <div class="foot-head" style="left:349px">SITEMAP</div>
  <ul class="foot-list" style="left:349px"><li>Home</li><li>About</li><li>Services</li><li>News</li><li>Contact Us</li></ul>
  <div class="foot-head" style="left:624px">SERVICES</div>
  <ul class="foot-list" style="left:624px"><li>Accounting</li><li>Bookkeeping</li><li>Tax Prep</li></ul>
  <div class="foot-head" style="left:899px">CONTACT US</div>
  <div class="foot-contact" style="top:100px"><svg width="20" height="16" viewBox="0 0 20 16" fill="none" stroke="#e9a21a" stroke-width="1.4"><rect x="1" y="1" width="18" height="14" rx="1"/><polyline points="1,2 10,9 19,2"/></svg>info@keystonegroup.com</div>
  <div class="foot-contact" style="top:142px"><svg width="20" height="20" viewBox="0 0 24 24"><path d="M6.6 10.8a15 15 0 0 0 6.6 6.6l2.2-2.2c.3-.3.7-.4 1-.2 1.1.4 2.3.6 3.6.6.6 0 1 .4 1 1V20c0 .6-.4 1-1 1A17 17 0 0 1 3 4c0-.6.4-1 1-1h3.5c.6 0 1 .4 1 1 0 1.3.2 2.5.6 3.6.1.3 0 .7-.2 1z" fill="none" stroke="#e9a21a" stroke-width="1.5"/></svg><span style="font-size:13px">123 456 7890</span></div>
  <div class="foot-contact" style="top:180px"><svg width="20" height="24" viewBox="0 0 20 24" fill="none" stroke="#e9a21a" stroke-width="1.5"><path d="M10 23s8-8 8-14a8 8 0 0 0-16 0c0 6 8 14 8 14z"/><circle cx="10" cy="9" r="3"/></svg><span style="font-size:11.5px">KEYSTONE GROUP<br>101 - lorem ipsum simple print.</span></div>

  <div class="abs" style="left:0;top:254px;width:1200px;height:1px;background:rgba(255,255,255,.08)"></div>
  <div class="abs" style="left:60px;top:285px;font-size:11px;color:#e8e8ea"><span style="color:var(--gold)">©KEYSTONE GROUP</span> - 2022 All rights reserved.</div>
  <div class="abs" style="left:1058px;top:283px;display:flex;gap:14px">
    <span style="width:14px;height:14px;border-radius:50%;background:var(--gold)"></span>
    <span style="width:14px;height:14px;border-radius:50%;background:var(--gold)"></span>
    <span style="width:14px;height:14px;border-radius:50%;background:var(--gold)"></span>
  </div>
</footer>

</body>
</html>
```